Invitation Design Project

I would like to have a custom invitation (and reception/response cards) designed for my son's Bar Mitzvah. I have a strong idea of what I want and have a few mock-ups, but my "home made" effort would be improved by the addition of professional creativity and skill. The invitation should be white, red, and black, and a bold typographic style (see attachment). I am looking for a clean modern feel, and prefer square shaped invitations. I need the final product in an electronic format that I could either print myself or have done at a local printer.

Target Market(s)

Guests to a Bar Mitzvah. A group of family and friends ranging from 40-60 years of age, and a group of my son's 13 year old friends.

Industry/Entity Type

Electronic

Requirements
Must have
• Square shaped invitation (exact dimensions in attached file)
Typographic style
Red, black, white
Red color should be CMYK: 30-96-76-26
Nice to have
• I like the two icons on my attached sample reception card, especially the swirl/Torah one. I would be nice to use these (or similar ones) if there is a way to do so, but this is not a requirement.

```html
<!DOCTYPE html>
<html lang="en">
<head>
<meta charset="utf-8">
<title>Reception Card</title>
<link rel="stylesheet" href="https://fonts.googleapis.com/css2?family=Bebas+Neue&family=Jost:wght@400;500;600&display=swap">
<style>
  :root {
    --red: #cf3539;
    --ink: #222222;
    --paper: #ffffff;
    --shade: #b9b9b9;
    --fold: #d9d9d9;
    --edge: #3a3a3a;
  }
  html, body {
    margin: 0;
    padding: 0;
    width: 1200px;
    height: 1200px;
    overflow: hidden;
    background: var(--paper);
  }
  .reception-card {
    display: block;
    width: 1200px;
    height: 1200px;
  }
  .backdrop { fill: var(--red); }
  .card-edge { fill: var(--edge); }
  .card { fill: var(--paper); }
  .banner { fill: var(--ink); }
  .banner-fold { fill: var(--fold); }
  .tag { fill: var(--red); }
  .banner-title {
    font-family: "Bebas Neue", "Oswald", sans-serif;
    fill: var(--paper);
    font-size: 92px;
  }
  .tag-label {
    font-family: "Jost", sans-serif;
    font-weight: 400;
    fill: var(--paper);
    font-size: 33px;
  }
  .details text {
    font-family: "Jost", sans-serif;
    fill: var(--ink);
  }
  .details {
    filter: drop-shadow(2px 2px 0 var(--shade));
  }
  .headline { font-weight: 500; font-size: 66px; }
  .invite-line { font-weight: 500; font-size: 30px; }
  .time { font-weight: 400; font-size: 84px; }
  .venue { font-weight: 500; font-size: 54px; }
  .address { font-weight: 500; font-size: 22px; }
</style>
</head>
<body>
<svg class="reception-card" viewBox="0 0 780 780" xmlns="http://www.w3.org/2000/svg">
  <rect class="backdrop" x="17" y="17" width="748" height="748"/>

  <rect class="card-edge" x="82" y="100" width="630" height="627"/>
  <rect class="card" x="77" y="95" width="630" height="625"/>

  <polygon class="banner-fold" points="47,345 77,345 77,360"/>
  <polygon class="banner-fold" points="707,255 735,252 707,272"/>
  <polygon class="banner" points="47,145 735,52 735,252 47,345"/>
  <text class="banner-title" x="392" y="232" text-anchor="middle" textLength="480" lengthAdjust="spacing" transform="rotate(-7.7 392 200)">RECEPTION</text>

  <rect class="tag" x="350" y="277" width="357" height="66"/>
  <text class="tag-label" x="528" y="322" text-anchor="middle">PLEASE JOIN US</text>

  <g class="details">
    <text class="headline" x="108" y="425" textLength="572" lengthAdjust="spacingAndGlyphs">PLEASE JOIN US</text>
    <text class="invite-line" x="108" y="466" textLength="572" lengthAdjust="spacing">for lunch, dancing and</text>
    <text class="invite-line" x="108" y="507" textLength="572" lengthAdjust="spacingAndGlyphs">celebration following the service</text>
    <text class="time" x="112" y="594" textLength="568" lengthAdjust="spacingAndGlyphs">1:00-4:30PM</text>
    <text class="venue" x="108" y="658" textLength="572" lengthAdjust="spacingAndGlyphs">The Lantern Hall</text>
    <text class="address" x="108" y="696" textLength="572" lengthAdjust="spacingAndGlyphs">2250 Maple Ridge Road, Fairview, VA 22000</text>
  </g>
</svg>
</body>
</html>
```